Stonebrook Inc Ad Design, trying to attract new customers

Please see attached pictures and files for information
We are a Class A - Residential General Contractor in Lynchburg, VA with Master HVAC and Master PLUMBING Licenses. We focus on Water and Air Solutions for property owners.
We build, remodel, and repair homes
We do HVAC, including Humidity Control and Air Purification
We do Plumbing
We love to fix Water Leaks for Plumbing, Roof Leaks, Skylight Leaks, Basement Leaks, Foundation Leaks, Door and Window Leaks
We solve water and air issues on the outside of properties with custom structures, grading, and landscaping

Target Market(s)

Residential and Light Commercial property owners

Industry/Entity Type

Construction

Font styles to use
Other font styles liked:
• see cards

Colors
0054AA
0677BA
7BADD7
CADEEF
E8F1F8
00AB8E
00BBA5
67D7C9
C6EFE9
E9F9F6

Requirements
Must have
• See business cards
Nice to have
• see business cards
Should not have
• My name

```html
<!DOCTYPE html>
<html lang="en">
<head>
<meta charset="utf-8">
<title>Stonebrook Inc Billboard</title>
<link rel="stylesheet" href="https://fonts.googleapis.com/css2?family=Montserrat:wght@700;800;900&family=Oswald:wght@600&family=Open+Sans:wght@600&display=swap">
<style>
  :root {
    --blue-deep: #0054AA;
    --blue-mid: #0677BA;
    --blue-light: #1a8fe0;
    --blue-text: #1658a8;
    --green-dark: #127228;
    --green-text: #1f7a1f;
    --green-sub: #5aa53a;
    --lime: #d4ff8a;
    --ink: #111111;
    --paper: #ffffff;
    --backdrop: #eef1f4;
  }
  * { box-sizing: border-box; margin: 0; padding: 0; }
  html, body { width: 1200px; height: 1200px; overflow: hidden; background: var(--backdrop); }
  .canvas { position: relative; width: 1200px; height: 1200px; }
  .billboard {
    position: absolute; left: 40px; top: 395px; width: 1120px; height: 410px;
    background: var(--paper); overflow: hidden;
    box-shadow: 0 6px 24px rgba(0,0,0,0.18);
  }
  .headline-band {
    position: absolute; left: 30px; right: 50px; top: 0; height: 64px;
    background: linear-gradient(90deg, var(--blue-deep), var(--blue-mid) 55%, var(--blue-light));
    border-radius: 0 0 18px 18px;
    display: flex; align-items: center; justify-content: center;
  }
  .headline {
    font-family: "Montserrat", sans-serif; font-weight: 900; font-size: 41px;
    color: var(--paper); letter-spacing: 0.5px; white-space: nowrap;
  }
  .brand {
    position: absolute; left: 30px; top: 160px; width: 380px;
    display: flex; flex-direction: column; align-items: center;
  }
  .brand-name {
    display: flex; align-items: center; gap: 12px;
    font-family: "Montserrat", sans-serif; font-weight: 800; font-size: 38px;
    color: var(--blue-deep); letter-spacing: 0.5px;
  }
  .brand-dot { width: 34px; height: 34px; border-radius: 50%; background: var(--green-text); }
  .badge {
    margin-top: 30px; background: var(--ink); color: var(--paper);
    font-family: "Open Sans", sans-serif; font-weight: 600; font-size: 15px;
    padding: 3px 10px; border-radius: 2px; letter-spacing: 0.3px;
  }
  .services {
    position: absolute; left: 420px; right: 30px; top: 76px;
    display: flex; flex-direction: column; align-items: center; text-align: center;
  }
  .tagline {
    font-family: "Oswald", sans-serif; font-weight: 600; font-size: 29px; line-height: 1.3;
    color: var(--green-sub); padding: 0 6px 4px; border-bottom: 2px solid var(--green-dark);
    white-space: nowrap;
  }
  .service-list { margin-top: 8px; list-style: none; }
  .service-list li {
    font-family: "Montserrat", sans-serif; font-weight: 800; font-size: 28px;
    line-height: 1.2; white-space: nowrap;
  }
  .service-list .blue { color: var(--blue-text); }
  .service-list .green { color: var(--green-text); }
  .contact-band {
    position: absolute; left: 0; right: 0; bottom: 0; height: 64px;
    background: var(--green-dark);
    display: flex; align-items: center; padding-left: 30px; gap: 70px;
  }
  .contact-item {
    display: flex; align-items: center; gap: 10px;
    font-family: "Montserrat", sans-serif; font-weight: 800; color: var(--lime);
    white-space: nowrap;
  }
  .contact-item.phone { font-size: 32px; }
  .contact-item.web { font-size: 38px; }
  .contact-item svg { flex: none; }
</style>
</head>
<body>
<main class="canvas">
  <section class="billboard" aria-label="Stonebrook Inc billboard">
    <header class="headline-band">
      <h1 class="headline">WATER &amp; AIR SOLUTIONS FOR YOUR HOME</h1>
    </header>

    <div class="brand">
      <div class="brand-name"><span class="brand-dot"></span>STONEBROOK</div>
      <div class="badge">LICENSED AND INSURED</div>
    </div>

    <div class="services">
      <p class="tagline">Class A - Residential General Contractor in Lynchburg, VA</p>
      <ul class="service-list">
        <li class="blue">Home Builds • Repairs • Remodeling</li>
        <li class="green">HVAC • Humidity • Air Purification</li>
        <li class="blue">Plumbing &amp; Leak Fixes -</li>
        <li class="blue">Roof, Basement, Foundation</li>
        <li class="green">Drainage • Grading • Landscaping</li>
      </ul>
    </div>

    <footer class="contact-band">
      <span class="contact-item phone">
        <svg width="30" height="30" viewBox="0 0 30 30" aria-hidden="true">
          <circle cx="15" cy="15" r="13" fill="none" stroke="#ffffff" stroke-width="2.5"/>
          <path d="M10 8c1-1 2-1 3 0l1.5 2.5c.5 1 0 1.8-.8 2.3-.5.3-.6.9-.3 1.4l2.4 2.4c.5.3 1.1.2 1.4-.3.5-.8 1.3-1.3 2.3-.8L22 17c1 1 1 2 0 3-2 2-5 1.5-8.5-2S8 10 10 8z" fill="#ffffff"/>
        </svg>
        (434) 555 0182
      </span>
      <span class="contact-item web">
        <svg width="32" height="32" viewBox="0 0 32 32" aria-hidden="true">
          <g fill="none" stroke="#ffffff" stroke-width="1.8">
            <circle cx="15" cy="15" r="12"/>
            <ellipse cx="15" cy="15" rx="5.5" ry="12"/>
            <line x1="3" y1="15" x2="27" y2="15"/>
            <path d="M5 9h20M5 21h20"/>
          </g>
          <path d="M20 18l9 4-4 1.2-1.5 4z" fill="#ffffff" stroke="#127228" stroke-width="1"/>
        </svg>
        www.StonebrookVA.com
      </span>
    </footer>
  </section>
</main>
</body>
</html>
```